Cedarline Coalition Web Presence Design and Relaunch

Take existing web files and "clean up" for a a more presentable web landing pad.
posted presently on a site pad CSS template. at www.cedarlinecoalition.org

The site is clunky and unprofessional looking. Needs to be toned down so the urgency is conveyed, but not via a burning planet image.

Target Market(s)

Non-profit climate adaptation group targeting local government land management agencies, special districts and private landholders of natural resource properties.

Industry/Entity Type

Environment

Coding

Coded - Design and coding required

Number of Pages Required

Font styles to use
Serif
Sans Serif

Requirements
Must have
• Include current logos, aspects if content on current site www.cedarlinecoalition.org
• A regional Pacific Northwest Focus (US & Canada). Content speaking to urgency but respectful of cultural diversity and norms. Sustainability themes. Emphasis on action and implementation.
Nice to have
• link to like minded projects. Appear to future generations. Diversity in thematic areas ecological resiliency, energy, food security and infrastructure.

```html
<!DOCTYPE html>
<html lang="en">
<head>
<meta charset="utf-8">
<title>Cedarline Coalition</title>
<link href="https://fonts.googleapis.com/css2?family=Roboto:ital,wght@0,400;0,500;0,700;1,400&display=swap" rel="stylesheet">
<style>
:root{
  --blue:#1b78bf;
  --blue-dark:#155f99;
  --green:#8dc63f;
  --green-band:#97c93d;
  --orange:#e4672b;
  --yellow:#f0b323;
  --text:#444;
  --muted:#666;
  --light:#eef1f3;
  --white:#fff;
}
*{margin:0;padding:0;box-sizing:border-box}
html,body{width:1200px;height:3949px;overflow:hidden}
body{position:relative;font-family:'Roboto',Arial,sans-serif;color:var(--text);background:var(--white)}
.abs{position:absolute}
a{color:inherit;text-decoration:none}

/* header */
.topline{left:0;top:0;width:1200px;height:5px;background:var(--blue)}
.header{left:0;top:5px;width:1200px;height:93px;background:var(--white);z-index:3}
.brand{left:107px;top:5px;width:140px;height:135px;border-radius:0 0 70px 70px;background:var(--white);z-index:4;display:flex;flex-direction:column;align-items:center;justify-content:center;gap:6px}
.brand-dot{width:22px;height:22px;border-radius:50%;background:var(--green)}
.brand-name{font-size:17px;font-weight:500;color:var(--blue);text-align:center;line-height:1.15}
.nav{left:420px;top:40px;display:flex;align-items:center;z-index:4;font-size:14.5px;font-weight:500;color:#222}
.nav a{margin-right:27px}
.nav .active{color:var(--green)}
.login{left:979px;top:31px;width:109px;height:39px;border-radius:20px;background:var(--green);color:#fff;font-size:15px;font-weight:500;display:flex;align-items:center;justify-content:center;z-index:4}

/* hero */
.hero{left:0;top:98px;width:1200px;height:546px;background:linear-gradient(180deg,#b9c7cf 0%,#7d9a86 30%,#4c8a54 55%,#3fa7a4 70%,#4f8c34 100%)}
.hero-title{left:0;top:250px;width:1200px;text-align:center;font-size:44px;font-weight:700;color:#fff}
.hero-sub{left:0;top:330px;width:1200px;text-align:center;font-size:18px;font-weight:500;color:#fff;line-height:29px}
.cta{left:501px;top:425px;width:199px;height:56px;border-radius:28px;background:var(--green);color:#fff;font-size:18px;font-weight:700;display:flex;align-items:center;justify-content:center;gap:8px}
.arrow{top:352px;width:35px;height:35px;border:2px solid #fff;border-radius:50%}

/* tiles */
.tile{top:644px;width:300px;height:306px;color:#fff;display:flex;flex-direction:column;align-items:center;justify-content:center;text-align:center;padding:0 22px}
.tile h3{font-size:18px;font-weight:500}
.tile p{font-size:13.5px;line-height:22px;margin-top:14px}
.t1{left:0;background:linear-gradient(180deg,#3f94cf,#2a77b5)}
.t2{left:300px;background:linear-gradient(180deg,#e77a3f,#d95f27)}
.t3{left:600px;background:linear-gradient(180deg,#f3bb36,#eaa81a)}
.t4{left:900px;background:linear-gradient(180deg,#9acd4b,#78b22e)}

/* section headings */
.heading{font-size:40px;font-weight:700;color:var(--blue)}
.heading span{color:var(--green);font-weight:400}
.divider{width:150px;height:14px}

/* about */
.tree{left:110px;top:1057px;width:434px;height:417px;background:radial-gradient(ellipse at 50% 35%,#a6d256 0%,#8dc63f 45%,#fff 72%);border-radius:8px}
.about-text{left:602px;top:1167px;width:488px;font-size:15px;line-height:28px;text-align:justify;color:var(--muted)}
.btn{height:48px;border-radius:24px;background:var(--green);color:#fff;font-size:14px;font-weight:700;display:flex;align-items:center;justify-content:center;gap:7px}

/* video */
.video{left:162px;top:1661px;width:876px;height:426px;background:radial-gradient(circle at 50% 50%,#6f8f5c 0%,#a9b7a2 30%,#d7dfe3 60%,#c9d3d8 100%)}
.play{left:567px;top:1842px;width:64px;height:64px;border-radius:50%;background:var(--blue)}

/* stats */
.stats{left:0;top:2190px;width:1200px;height:267px;background:var(--green-band)}
.stat{top:2228px;width:260px;text-align:center;color:#fff}
.stat .num{font-size:30px;font-weight:500}
.stat .ring{width:96px;height:96px;border-radius:50%;background:#fff;margin:14px auto 0;display:flex;align-items:center;justify-content:center}
.stat .core{width:80px;height:80px;border-radius:50%;background:var(--blue);border:3px solid #fff;box-shadow:0 0 0 2px var(--blue)}
.stat .label{font-size:19px;font-weight:500;margin-top:16px}

/* think green */
.green-text{left:110px;top:2612px;width:469px;font-size:15px;line-height:28px;text-align:justify;color:var(--muted)}
.chart{left:620px;top:2550px}

/* recent work */
.work{left:0;top:2992px;width:1200px;height:553px;background:var(--light)}
.work-intro{left:0;top:3126px;width:1200px;text-align:center;font-size:15px;line-height:22px;color:var(--muted)}
.card{top:3199px;width:232px;text-align:center}
.card .photo{height:208px;border:4px solid #fff;box-shadow:0 0 0 1px #d7dbde}
.card.active .photo{border-color:#8dc63f}
.card h4{font-size:19px;font-weight:500;color:#222;margin-top:20px}
.card em{display:block;font-size:15px;color:var(--muted);margin-top:4px}

/* footer */
.footer{left:0;top:3545px;width:1200px;height:404px;background:linear-gradient(180deg,#1b7fc7,#1a74b8);color:#fff}
.foot-brand{left:110px;top:3640px;display:flex;align-items:center;gap:10px}
.foot-brand .dot{width:20px;height:20px;border-radius:50%;background:#fff}
.foot-brand .name{font-size:18px;font-weight:500;line-height:1.15}
.foot-about{left:110px;top:3725px;width:285px;font-size:13px;line-height:20px}
.foot-h{font-size:16px;font-weight:500;text-transform:uppercase}
.foot-list{list-style:none;font-size:15px}
.foot-list li{height:29px;display:flex;align-items:center;gap:10px}
.contact li{align-items:flex-start;height:auto;margin-bottom:14px;line-height:23px}
.social li{height:45px;gap:14px}
.social .circ{width:36px;height:36px;border-radius:50%;background:rgba(255,255,255,.18);border:2px solid rgba(255,255,255,.5)}
.rule{left:110px;top:3865px;width:978px;height:1px;background:rgba(255,255,255,.5)}
.copy{left:0;top:3894px;width:1200px;text-align:center;font-size:15px}
</style>
</head>
<body>

<div class="abs topline"></div>
<header class="abs header"></header>
<div class="abs brand">
  <div class="brand-dot"></div>
  <div class="brand-name">CEDARLINE<br>COALITION</div>
</div>
<nav class="abs nav">
  <a class="active">Home</a><a>About Us</a><a>What We Do</a><a>Careers</a><a>News</a><a>Contact Us</a>
  <svg width="16" height="16" viewBox="0 0 16 16"><circle cx="6.5" cy="6.5" r="4.8" fill="none" stroke="#222" stroke-width="2"/><line x1="10" y1="10" x2="14.5" y2="14.5" stroke="#222" stroke-width="2.4"/></svg>
</nav>
<a class="abs login">
  <svg width="12" height="14" viewBox="0 0 12 14" style="margin-right:8px"><rect x="1" y="6" width="10" height="7.5" rx="1" fill="#fff"/><path d="M3 6V4a3 3 0 0 1 6 0" fill="none" stroke="#fff" stroke-width="1.6"/></svg>Login</a>

<section class="abs hero" role="img" aria-label="Mountain lake valley with turquoise water, evergreen forest and snowy peaks"></section>
<h1 class="abs hero-title">Implementing Climate Strategies</h1>
<p class="abs hero-sub">Dedicated to taking action the Cedarline Coalition was created<br>to help bring adaption strategies to life.</p>
<a class="abs cta">GET STARTED
  <svg width="17" height="17" viewBox="0 0 17 17"><circle cx="8.5" cy="8.5" r="8" fill="#fff"/><path d="M6 5l4 3.5L6 12" fill="none" stroke="#8dc63f" stroke-width="2.2"/></svg></a>
<div class="abs arrow" style="left:35px"><svg width="31" height="31" viewBox="0 0 31 31"><path d="M18 9l-6 6.5 6 6.5" fill="none" stroke="#fff" stroke-width="2"/></svg></div>
<div class="abs arrow" style="left:1126px"><svg width="31" height="31" viewBox="0 0 31 31"><path d="M13 9l6 6.5-6 6.5" fill="none" stroke="#fff" stroke-width="2"/></svg></div>

<div class="abs tile t1"><h3>Adaptation Plans</h3></div>
<div class="abs tile t2"><h3>On The Ground</h3><p>The Alliance is familiar and growing throughout the region. Presently our work has us on the ground in keystone watersheds in the Cascade, Willamette, Columbia and Boise basin watersheds.</p></div>
<div class="abs tile t3"><h3>Ecological Resilience</h3></div>
<div class="abs tile t4"><h3>Energy And Food</h3></div>

<div class="abs tree" role="img" aria-label="Illustration of a blue-trunked tree with green leaves"></div>
<h2 class="abs heading" style="left:602px;top:1075px">About <span>Us</span></h2>
<svg class="abs divider" style="left:602px;top:1124px" viewBox="0 0 150 14"><line x1="0" y1="7" x2="50" y2="7" stroke="#e4672b" stroke-width="2"/><circle cx="75" cy="7" r="6" fill="#8dc63f"/><line x1="100" y1="7" x2="150" y2="7" stroke="#e4672b" stroke-width="2"/></svg>
<p class="abs about-text">Founded in 2019, the Cedarline Coalition draws from decades of commitment and action. A core group of committed professionals and community leaders have come together to grow and build a network of people who want to secure our next generations future. Members of the Alliance come from all backgrounds and ages, but all commonly believe we can no longer be just “scribes and witnesses” to the pending demise. We believe in answering the call to action.</p>
<a class="abs btn" style="left:602px;top:1400px;width:172px">VOLUNTEERS
  <svg width="14" height="14" viewBox="0 0 17 17"><circle cx="8.5" cy="8.5" r="8" fill="#fff"/><path d="M6 5l4 3.5L6 12" fill="none" stroke="#8dc63f" stroke-width="2.2"/></svg></a>

<h2 class="abs heading" style="left:0;top:1557px;width:1200px;text-align:center">What We <span>Are Doing ?</span></h2>
<svg class="abs divider" style="left:525px;top:1611px" viewBox="0 0 150 14"><line x1="0" y1="7" x2="50" y2="7" stroke="#e4672b" stroke-width="2"/><circle cx="75" cy="7" r="6" fill="#8dc63f"/><line x1="100" y1="7" x2="150" y2="7" stroke="#e4672b" stroke-width="2"/></svg>
<div class="abs video" role="img" aria-label="Hand holding a glass sphere reflecting a forest"></div>
<div class="abs play"><svg width="64" height="64" viewBox="0 0 64 64"><path d="M25 19l21 13-21 13z" fill="#fff"/></svg></div>

<section class="abs stats"></section>
<div class="abs stat" style="left:89px"><div class="num">250 +</div><div class="ring"><div class="core"></div></div><div class="label">Projects Completed</div></div>
<div class="abs stat" style="left:354px"><div class="num">300 +</div><div class="ring"><div class="core"></div></div><div class="label">Donations</div></div>
<div class="abs stat" style="left:619px"><div class="num">17 +</div><div class="ring"><div class="core"></div></div><div class="label">Communities engaged</div></div>
<div class="abs stat" style="left:883px"><div class="num">70 +</div><div class="ring"><div class="core"></div></div><div class="label">Volunteers</div></div>

<h2 class="abs heading" style="left:110px;top:2541px">Think Green ! <span>Save Money</span></h2>
<p class="abs green-text">Lorem ipsum dolor sit amet, consectetur adipiscing elit, sed do eiusmod tempor incididunt ut labore et dolore magna aliqua. Ut enim ad minim veniam, quis nostrud exercitation ullamco laboris nisi ut aliquip ex ea commodo consequat. Duis aute irure dolor in reprehenderit in voluptate velit esse cillum dolore eu fugiat nulla pariatur. Excepteur sint occaecat cupidatat non proident, sunt in culpa qui officia deserunt mollit anim id est laborum.</p>
<a class="abs btn" style="left:110px;top:2844px;width:167px">LEARN MORE
  <svg width="14" height="14" viewBox="0 0 17 17"><circle cx="8.5" cy="8.5" r="8" fill="#fff"/><path d="M6 5l4 3.5L6 12" fill="none" stroke="#8dc63f" stroke-width="2.2"/></svg></a>

<svg class="abs chart" width="500" height="370" viewBox="0 0 500 370" font-family="Roboto, Arial, sans-serif">
  <defs>
    <linearGradient id="barBody" x1="0" x2="1"><stop offset="0" stop-color="#1b74b4"/><stop offset=".5" stop-color="#1f86c8"/><stop offset="1" stop-color="#155f99"/></linearGradient>
  </defs>
  <g font-size="15" fill="#333" text-anchor="middle">
    <!-- Clean Water 98% -->
    <text x="65" y="22">98%</text>
    <path d="M39 58v247l26 8 26-8V58z" fill="url(#barBody)"/>
    <path d="M39 58l26-14 26 14-26 14z" fill="#b9c3ee"/>
    <path d="M39 58l26 14v14L39 72z" fill="#3aa3c9"/><path d="M91 58L65 72v14l26-14z" fill="#2b8fbd"/>
    <text x="65" y="340">Clean Water</text>
    <!-- Forest Rescue 56% -->
    <text x="183" y="115">56%</text>
    <path d="M157 149v156l26 8 26-8V149z" fill="url(#barBody)"/>
    <path d="M157 149l26-14 26 14-26 14z" fill="#b9c3ee"/>
    <path d="M157 149l26 14v14l-26-14z" fill="#3aa3c9"/><path d="M209 149l-26 14v14l26-14z" fill="#2b8fbd"/>
    <text x="183" y="340">Forest Rescue</text>
    <!-- Agriculture 77% -->
    <text x="303" y="80">77%</text>
    <path d="M277 114v191l26 8 26-8V114z" fill="url(#barBody)"/>
    <path d="M277 114l26-14 26 14-26 14z" fill="#b9c3ee"/>
    <path d="M277 114l26 14v14l-26-14z" fill="#3aa3c9"/><path d="M329 114l-26 14v14l26-14z" fill="#2b8fbd"/>
    <text x="303" y="340">Agriculture</text>
    <!-- Alternative Energy 84% -->
    <text x="421" y="62">84%</text>
    <path d="M395 97v208l26 8 26-8V97z" fill="url(#barBody)"/>
    <path d="M395 97l26-14 26 14-26 14z" fill="#b9c3ee"/>
    <path d="M395 97l26 14v14l-26-14z" fill="#3aa3c9"/><path d="M447 97l-26 14v14l26-14z" fill="#2b8fbd"/>
    <text x="421" y="340">Alternative</text>
    <text x="421" y="358">Energy</text>
  </g>
</svg>

<section class="abs work"></section>
<h2 class="abs heading" style="left:0;top:3036px;width:1200px;text-align:center">Recent <span>Work</span></h2>
<svg class="abs divider" style="left:525px;top:3089px" viewBox="0 0 150 14"><line x1="0" y1="7" x2="50" y2="7" stroke="#e4672b" stroke-width="2"/><circle cx="75" cy="7" r="6" fill="#8dc63f"/><line x1="100" y1="7" x2="150" y2="7" stroke="#e4672b" stroke-width="2"/></svg>
<p class="abs work-intro">Sed ut perspiciatis unde omnis iste natus error sit voluptatem accusantium doloremque laudantium, totam<br>rem aperiam, eaque ipsa quae ab illo inventore veritatis et quasi</p>
<div class="abs card active" style="left:111px"><div class="photo" role="img" aria-label="Wind turbine against a dusky mountain sky" style="background:linear-gradient(180deg,#6b6a70,#8d7a6a 60%,#4c4a48)"></div><h4>Energy</h4><em>Investing in clean energy</em></div>
<div class="abs card" style="left:360px"><div class="photo" role="img" aria-label="Hand placing blue sky tiles over a golden wheat field" style="background:linear-gradient(180deg,#8a8c90 0%,#7f9ccc 45%,#d9b43c 75%,#b39630)"></div><h4>Food Security</h4><em>Retooling agriculture</em></div>
<div class="abs card" style="left:608px"><div class="photo" role="img" aria-label="Aerial view of a river delta wetland" style="background:linear-gradient(180deg,#7d97a8,#a6773f 50%,#5e5036)"></div><h4>Ecological Resilience</h4><em>Environmental Progress</em></div>
<div class="abs card" style="left:857px"><div class="photo" role="img" aria-label="Hand holding a phone showing a forest road" style="background:linear-gradient(180deg,#2f3a2c,#4d5a48 50%,#2a2a2a)"></div><h4>Infrastructure</h4><em>Lorem Ipsum</em></div>

<footer class="abs footer"></footer>
<div class="abs foot-brand" style="color:#fff"><div class="dot"></div><div class="name">CEDARLINE<br>COALITION</div></div>
<p class="abs foot-about" style="color:#fff">We are hyper focused on Implementation. We are eager to get about the business of preparing communities in the Pacific Northwest for fundamental change brought on by shifts in our climate and ecology.</p>

<h5 class="abs foot-h" style="left:440px;top:3620px;color:#fff">Quick Links</h5>
<ul class="abs foot-list" style="left:440px;top:3652px;color:#fff">
  <li><span>»</span>About Us</li><li><span>»</span>Causes</li><li><span>»</span>Testimonial</li><li><span>»</span>Events</li><li><span>»</span>Contact Us</li>
</ul>

<h5 class="abs foot-h" style="left:642px;top:3614px;color:#fff">Contact Us</h5>
<ul class="abs foot-list contact" style="left:648px;top:3655px;width:240px;color:#fff">
  <li><svg width="12" height="16" viewBox="0 0 12 16" style="margin-top:4px;flex:none"><path d="M6 15S1 9 1 6a5 5 0 0 1 10 0c0 3-5 9-5 9z" fill="#fff"/><circle cx="6" cy="6" r="2" fill="#1a7bc2"/></svg><span>418 Alder Street,<br>Riverbend WA 98201</span></li>
  <li><svg width="12" height="16" viewBox="0 0 12 16" style="margin-top:4px;flex:none"><rect x="2" y="1" width="8" height="14" rx="1.5" fill="none" stroke="#fff" stroke-width="1.6"/></svg><span>(123) 555-0142</span></li>
  <li><svg width="14" height="14" viewBox="0 0 14 14" style="margin-top:4px;flex:none"><rect x="1" y="3" width="12" height="10" rx="1" fill="#fff"/><rect x="3" y="1" width="8" height="3" fill="#fff"/></svg><span>555 555 0199</span></li>
  <li><svg width="14" height="12" viewBox="0 0 14 12" style="margin-top:6px;flex:none"><rect x="1" y="1" width="12" height="10" fill="none" stroke="#fff" stroke-width="1.5"/><path d="M1 1l6 5 6-5" fill="none" stroke="#fff" stroke-width="1.5"/></svg><span>info@cedarlinecoalition.org</span></li>
</ul>

<h5 class="abs foot-h" style="left:935px;top:3620px;color:#fff">Socail Media</h5>
<ul class="abs foot-list social" style="left:935px;top:3656px;color:#fff">
  <li><span class="circ"></span>Gatherly</li><li><span class="circ"></span>Circleplus</li><li><span class="circ"></span>Reelcast</li><li><span class="circ"></span>Chirpline</li>
</ul>

<div class="abs rule"></div>
<p class="abs copy" style="color:#fff">© 2020 Cedarline Coalition &nbsp;| All Rights Reserved | Terms and Conditions</p>

</body>
</html>
```